Remodeling brochure

We need an informative homeowner friendly brochure detailing our company and things we do. We are looking for an initial setup and ideas (# of pages, etc) and then we will send more content. We are uploading our logo design. We are a high end remodeling company specializing in kitchen & bath remodels. We sell ourselves on customer communication and attention to detail in our designs and remodels.

Target Market(s)

Residential homeowners

Contact Information for Business Card

Modern and attention grabbing

Requirements
Must have
• Name- Hearth & Tile Crafters<br/>Address- 782 NW Larkspur Lane Suite #217<br/> Ankeny, Iowa 50894<br/>Phone- 515-482-7395<br/>email-htcraftersmidwest@pinemail.net

```html
<!DOCTYPE html>
<html lang="en">
<head>
<meta charset="utf-8">
<title>Hearth &amp; Tile Crafters – Remodeling Brochure Spread</title>
<link rel="stylesheet" href="https://fonts.googleapis.com/css2?family=Open+Sans:wght@400;600;700;800&display=swap">
<style>
  :root{
    --canvas:#cfcfcf;
    --paper:#f4f4f4;
    --blue:#1e7bc8;
    --blue-light:#3aa0e0;
    --blue-deep:#1457a8;
    --indigo:#3f4fa8;
    --ink:#1c1c1c;
    --text-grey:#555;
    --light-text:#e8e8e8;
    --slate:#4a5260;
    --navy:#1d2330;
    --photo-warm:#b99b7a;
    --photo-cream:#d9cdbb;
    --photo-cool:#c9d0d6;
    --photo-brown:#6f5442;
  }
  *{box-sizing:border-box;margin:0;padding:0}
  html,body{width:1200px;height:833px;overflow:hidden}
  body{background:var(--canvas);font-family:"Open Sans",Arial,sans-serif;position:relative}
  .spread{position:absolute;left:80px;top:51px;width:1040px;height:730px;display:flex;box-shadow:0 6px 24px rgba(0,0,0,.18)}
  .page{position:relative;width:520px;height:730px;background:var(--paper);overflow:hidden}
  .page svg.bg{position:absolute;inset:0;width:520px;height:730px}
  .abs{position:absolute}
  .photo{position:absolute}
  .photo-warm{background:linear-gradient(135deg,var(--photo-cream),var(--photo-warm))}
  .photo-cool{background:linear-gradient(135deg,#e6eaee,var(--photo-cool))}
  .photo-brown{background:linear-gradient(135deg,var(--photo-warm),var(--photo-brown))}
  .tile-slate{position:absolute;background:var(--slate)}
  .tile-navy{position:absolute;background:var(--navy)}

  .headline{left:48px;top:84px;color:var(--blue);line-height:1;letter-spacing:1px;font-weight:400}
  .headline .big{display:block;font-size:33px}
  .headline .small{display:block;font-size:20px;margin:2px 0 3px 14px}
  .headline .indent{margin-left:-6px}

  .section-title{left:48px;top:232px;color:var(--ink)}
  .section-title h2{font-size:17px;font-weight:800;letter-spacing:.3px}
  .section-title h3{font-size:12px;font-weight:800;margin-top:2px}
  .rule{left:48px;top:280px;width:210px;height:1px;background:var(--ink)}
  .body-copy{left:48px;top:294px;width:360px;font-size:7.6px;line-height:1.35;color:var(--text-grey);text-align:center}
  .body-copy p{margin-bottom:7px}

  .offers-title{left:250px;top:104px;font-size:30px;color:var(--blue);letter-spacing:2px;font-weight:400}
  .offer-list{left:250px;top:160px;width:240px;list-style:none}
  .offer-list li{display:flex;gap:12px;margin-bottom:18px}
  .offer-list .mark{flex:none;width:22px;height:22px;background:linear-gradient(135deg,var(--blue-light),var(--blue-deep))}
  .offer-list strong{display:block;font-size:9.5px;font-weight:600;color:var(--ink)}
  .offer-list span{display:block;font-size:6.4px;color:var(--text-grey);line-height:1.3}

  .overview-label{left:52px;top:470px;font-size:9px;color:var(--light-text);letter-spacing:.5px}
  .overview-box{left:36px;top:486px;width:250px;height:92px;background:linear-gradient(135deg,#2f7fd0,var(--indigo));padding:10px 14px;color:#fff}
  .overview-box .field{font-size:9.5px;font-weight:700;height:26px;border-bottom:1px solid rgba(255,255,255,.85);padding-top:2px;margin-bottom:2px}
  .overview-box .field:last-child{border-bottom:none}
  .dark-offers-title{left:318px;top:500px;font-size:17px;color:#fff;letter-spacing:1.5px;font-weight:400}
  .dark-offers{left:308px;top:534px;width:192px;list-style:none;color:var(--light-text);font-size:7.4px;line-height:1.35}
  .dark-offers li{border-bottom:1px solid #8a8a8a;padding:4px 0 5px}
  .dark-copy{left:40px;top:642px;width:440px;font-size:7.6px;line-height:1.45;color:var(--light-text);text-align:center}
</style>
</head>
<body>
<main class="spread">

  <section class="page page-left">
    <svg class="bg" viewBox="0 0 520 730" aria-hidden="true">
      <defs>
        <linearGradient id="bandL" x1="0" x2="1"><stop offset="0" stop-color="#1457a8"/><stop offset="1" stop-color="#3aa0e0"/></linearGradient>
        <linearGradient id="hexFill" x1="0" y1="0" x2="1" y2="1"><stop offset="0" stop-color="#3aa0e0"/><stop offset="1" stop-color="#1457a8"/></linearGradient>
        <linearGradient id="darkL" x1="0" x2="1"><stop offset="0" stop-color="#4a4a4a"/><stop offset="1" stop-color="#262626"/></linearGradient>
      </defs>
      <path d="M0 0 H520 V34 Q260 4 0 12 Z" fill="url(#bandL)"/>
      <path d="M0 20 Q260 10 520 40 V44 Q260 16 0 24 Z" fill="#ffffff"/>
    </svg>

    <div class="photo photo-warm" style="left:300px;top:70px;width:100px;height:100px" role="img" aria-label="Photo: technician installing a bathroom fixture"></div>
    <div class="tile-slate" style="left:405px;top:70px;width:115px;height:100px"></div>
    <div class="photo photo-cool" style="left:270px;top:176px;width:125px;height:100px" role="img" aria-label="Photo: hand adjusting a chrome shower valve"></div>
    <div class="photo photo-brown" style="left:400px;top:176px;width:120px;height:100px" role="img" aria-label="Photo: modern bathroom vanity and tiled wall"></div>

    <svg class="abs" style="left:222px;top:100px" width="90" height="90" viewBox="0 0 90 90" aria-hidden="true">
      <polygon points="22,4 68,4 90,45 68,86 22,86 0,45" fill="url(#hexFill)"/>
    </svg>

    <h1 class="abs headline">
      <span class="big">DREAMS</span>
      <span class="small">DON'T WORK</span>
      <span class="big indent">UNLESS</span>
      <span class="big indent">YOU DO !!</span>
    </h1>

    <div class="abs section-title">
      <h2>BRAND POSITIONING</h2>
      <h3>BRAND POSITIONING</h3>
    </div>
    <div class="abs rule"></div>
    <div class="abs body-copy">
      <p>Lorem ipsum dolor sit amet, consectetuer adipiscing elit, sed diam nonummy nibh euismod tincidunt ut laoreet dolore magna aliquam erat volutpat. Ut wisi enim ad minim veniam, quis nostrud exerci tation ullamcorper suscipit lobortis nisl ut aliquip ex ea commodo consequat.</p>
      <p>Duis autem vel eum iriure dolor in hendrerit in vulputate velit esse molestie consequat, vel illum dolore eu feugiat nulla facilisis at vero eros et accumsan et iusto odio dignissim qui blandit praesent luptatum zzril delenit augue duis dolore te feugait nulla facilisi.</p>
      <p>Lorem ipsum dolor sit amet, cons ectetuer adipiscing elit, sed diam nonummy nibh euismod tincidunt ut laoreet dolore magna aliquam erat volutpat. Ut wisi enim ad minim veniam, quis nostrud exerci tation ullamcorper suscipit lobortis nisl ut aliquip ex ea commodo consequat.</p>
    </div>

    <div class="photo" style="left:0;top:470px;width:520px;height:260px;background:linear-gradient(160deg,#e8ecee 0%,#cbbfa8 45%,#8d7a62 100%)" role="img" aria-label="Photo: granite kitchen countertop with cooktop by a bright window"></div>
    <svg class="bg" viewBox="0 0 520 730" aria-hidden="true">
      <path d="M0 470 H520 V520 Q420 500 330 530 Q200 560 0 470 Z" fill="#f4f4f4"/>
      <polygon points="0,440 100,470 0,500" fill="url(#hexFill)"/>
      <path d="M330 730 Q420 620 520 600 V730 Z" fill="url(#darkL)"/>
    </svg>
  </section>

  <section class="page page-right">
    <svg class="bg" viewBox="0 0 520 730" aria-hidden="true">
      <defs>
        <linearGradient id="bandR" x1="0" x2="1"><stop offset="0" stop-color="#3aa0e0"/><stop offset="1" stop-color="#1457a8"/></linearGradient>
        <linearGradient id="darkR" x1="0" y1="0" x2="1" y2="1"><stop offset="0" stop-color="#262626"/><stop offset=".5" stop-color="#454545"/><stop offset="1" stop-color="#1e1e1e"/></linearGradient>
      </defs>
      <path d="M0 40 Q260 10 520 34 V0 H0 Z" fill="url(#bandR)"/>
      <path d="M0 44 Q260 16 520 40 V46 Q260 22 0 50 Z" fill="#ffffff"/>
      <path d="M0 470 Q200 380 520 380 V730 H0 Z" fill="url(#darkR)"/>
    </svg>

    <div class="tile-navy" style="left:0;top:92px;width:60px;height:92px"></div>
    <div class="photo photo-warm" style="left:65px;top:88px;width:140px;height:96px" role="img" aria-label="Photo: open kitchen with island and wood cabinets"></div>
    <div class="photo photo-brown" style="left:0;top:190px;width:60px;height:110px" role="img" aria-label="Photo: dark vanity cabinet detail"></div>
    <div class="photo photo-brown" style="left:65px;top:190px;width:140px;height:110px" role="img" aria-label="Photo: remodeled kitchen with dark island"></div>

    <h2 class="abs offers-title">OUR OFFERS</h2>
    <ul class="abs offer-list">
      <li><i class="mark"></i><div><strong>Lorem ipsum dolor sit amet, consectetuer</strong><span>Lorem ipsum dolor sit amet, consectetuer adipiscing elit, sed diam nonummy nibh euismod tincidunt ut laoreet dolore</span></div></li>
      <li><i class="mark"></i><div><strong>Lorem ipsum dolor sit amet, consectetuer</strong><span>Lorem ipsum dolor sit amet, consectetuer adipiscing elit, sed diam nonummy nibh euismod tincidunt ut laoreet dolore</span></div></li>
      <li><i class="mark"></i><div><strong>Lorem ipsum dolor sit amet, consectetuer</strong><span>Lorem ipsum dolor sit amet, consectetuer adipiscing elit, sed diam nonummy nibh euismod tincidunt ut laoreet dolore</span></div></li>
    </ul>

    <p class="abs overview-label">OVER VIEW</p>
    <div class="abs overview-box">
      <div class="field">Project Name :</div>
      <div class="field">Client :</div>
      <div class="field">Category :</div>
    </div>

    <h2 class="abs dark-offers-title">OUR OFFERS</h2>
    <ul class="abs dark-offers">
      <li>Lorem ipsum dolor sit amet, consectetuer adipiscing elit, sed diam nonummy nibh euismod</li>
      <li>Lorem ipsum dolor sit amet, consectetuer adipiscing elit, sed diam nonummy nibh euismod</li>
      <li>Lorem ipsum dolor sit amet, consectetuer adipiscing elit, sed diam nonummy nibh euismod</li>
    </ul>

    <p class="abs dark-copy">Lorem ipsum dolor sit amet, consectetuer adipiscing elit, sed diam nonummy nibh euismod tincidunt ut laoreet dolore magna aliquam erat volutpat. Ut wisi enim ad minim veniam, quis nostrud exerci tation ullamcorper suscipit lobortis nisl ut aliquip ex ea commodo consequat. Duis autem vel eum iriure dolor in hendrerit in vulputate velit esse molestie consequat, vel illum</p>
  </section>

</main>
</body>
</html>
```